Stationery Design Project for import company - Tallo Goods

We are a import company that sells branded products to large retailers in New Zealand.
We need a simple, professional looking Logo, Business Cards, Email Signature and Letterhead.
Design needs to have some colour in it but nothing too bright or youthful.
The brand is business to business.
The companies name is Tallo Goods.
I have uploaded some examples of business cards that I like
Also need a powerpoint template
The range of products is diverse so the deign needs to be generic. Please note that the business does not sell to consumers only other businesses
Target Market(s)
Buyers at Retail Companies Head Offices (business to business)
Industry/Entity Type
Business
Look and feel
Each slider illustrates characteristics of the customer's brand and the style your logo design should communicate.

```html
<!DOCTYPE html>
<html lang="en">
<head>
<meta charset="utf-8">
<title>Tallo Goods Stationery</title>
<link rel="stylesheet" href="https://fonts.googleapis.com/css2?family=Montserrat:wght@700&family=Questrial&display=swap">
<style>
  :root {
    --brand-blue: #1d4490;
    --brand-black: #0b0b0b;
    --navy: #16336b;
    --navy-glow: #2551a8;
    --header-grey: #f3f4f8;
    --paper: #ffffff;
    --watermark: #eef0f6;
    --stage: #ffffff;
    --ink: #111111;
    --logo-light: #c9d3e6;
  }
  * { margin: 0; padding: 0; box-sizing: border-box; }
  html, body { width: 1200px; height: 1200px; overflow: hidden; background: var(--stage); }
  body { position: relative; font-family: "Questrial", "Century Gothic", sans-serif; color: var(--ink); }

  .piece { position: absolute; background: var(--paper); overflow: hidden; box-shadow: 0 0 0 1px #e4e6ec; }
  .band { position: absolute; display: block; }
  .band svg { display: block; width: 100%; height: 100%; }

  .wordmark { font-family: "Montserrat", sans-serif; font-weight: 700; color: var(--brand-blue); text-transform: uppercase; letter-spacing: 0.02em; white-space: nowrap; line-height: 1; }
  .person-name { font-family: "Montserrat", sans-serif; font-weight: 700; color: var(--brand-blue); line-height: 1; white-space: nowrap; }
  .person-role { font-size: 9px; text-align: right; text-transform: uppercase; line-height: 1; }
  .contact-list { list-style: none; font-size: 11px; text-transform: uppercase; line-height: 14px; }
  .contact-list li { display: flex; align-items: center; gap: 6px; white-space: nowrap; }
  .contact-list svg { width: 11px; height: 9px; flex: none; }

  /* Letterhead */
  .letterhead { left: 22px; top: 46px; width: 611px; height: 786px; }
  .letterhead .band-top { left: 0; top: 0; width: 611px; height: 44px; }
  .letterhead .header-strip { position: absolute; left: 0; top: 44px; width: 611px; height: 88px; background: var(--header-grey); }
  .letterhead .wordmark { position: absolute; left: 48px; top: 54px; font-size: 22px; }
  .letterhead .person { position: absolute; left: 260px; top: 34px; width: 118px; }
  .letterhead .person-name { font-size: 14px; }
  .letterhead .contact-list { position: absolute; left: 398px; top: 30px; }
  .letterhead .watermark { position: absolute; left: 110px; top: 370px; width: 392px; text-align: center; font-family: "Montserrat", sans-serif; font-weight: 700; font-size: 56px; color: var(--watermark); text-transform: uppercase; line-height: 1; }
  .letterhead .band-bottom { left: 0; top: 741px; width: 611px; height: 45px; }
  .letterhead .footer-url { position: absolute; left: 372px; top: 747px; color: #fff; font-size: 14px; letter-spacing: 0.03em; }

  /* Business card front */
  .card-front { left: 652px; top: 150px; width: 520px; height: 300px; background: radial-gradient(ellipse at 50% 38%, var(--navy-glow) 0%, var(--navy) 70%); box-shadow: none; }
  .card-front .wordmark { position: absolute; left: 0; width: 100%; top: 128px; text-align: center; font-size: 46px; color: var(--logo-light); }

  /* Business card back */
  .card-back { left: 674px; top: 503px; width: 500px; height: 285px; }
  .card-back .wordmark { position: absolute; left: 28px; top: 128px; font-size: 22px; }
  .card-back .divider { position: absolute; left: 246px; top: 105px; width: 2px; height: 75px; background: var(--brand-blue); }
  .card-back .person { position: absolute; left: 275px; top: 104px; width: 155px; }
  .card-back .person-name { font-size: 17px; }
  .card-back .person-role { font-size: 11px; }
  .card-back .contact-list { position: absolute; left: 275px; top: 141px; }

  /* Envelope front */
  .envelope-front { left: 28px; top: 900px; width: 552px; height: 262px; }
  .envelope-front .band-top { left: 0; top: 0; width: 552px; height: 44px; }
  .envelope-front .wordmark { position: absolute; left: 44px; top: 118px; font-size: 20px; }
  .envelope-front .person { position: absolute; left: 56px; top: 178px; width: 100px; }
  .envelope-front .person-name { font-size: 12px; }
  .envelope-front .person-role { font-size: 7px; }
  .envelope-front .contact-list { position: absolute; left: 56px; top: 200px; font-size: 9px; line-height: 12px; }
  .envelope-front .band-bottom { left: 0; top: 236px; width: 552px; height: 26px; }

  /* Envelope back */
  .envelope-back { left: 590px; top: 880px; width: 550px; height: 270px; }
  .envelope-back .flap-lines { position: absolute; inset: 0; width: 100%; height: 100%; }
  .envelope-back .wordmark { position: absolute; left: 0; width: 100%; top: 78px; text-align: center; font-size: 14px; color: var(--brand-black); }
  .envelope-back .band-bottom { left: 0; top: 244px; width: 550px; height: 26px; }
</style>
</head>
<body>

<section class="piece letterhead" aria-label="Letterhead">
  <span class="band band-top"><svg viewBox="0 0 611 44" preserveAspectRatio="none"><polygon points="0,0 338,0 306,44 0,44" fill="var(--brand-blue)"/><polygon points="344,0 611,0 611,44 312,44" fill="var(--brand-black)"/></svg></span>
  <div class="header-strip">
    <div class="wordmark">Tallo Goods</div>
    <div class="person"><div class="person-name">YOUR NAME.....</div><div class="person-role">Position</div></div>
    <ul class="contact-list">
      <li><svg viewBox="0 0 11 9"><path d="M0 3 Q5.5 -1 11 3 L9 4 L7.5 2.5 L3.5 2.5 L2 4 Z M2 5 H9 V9 H2 Z" fill="var(--ink)"/></svg>00 0000 0000</li>
      <li><svg viewBox="0 0 11 9"><rect x="0" y="1" width="11" height="7" fill="var(--ink)"/><path d="M0 1 L5.5 5 L11 1" stroke="#fff" fill="none"/></svg>EMAILADDRESS@DOMAIN.COM</li>
      <li><svg viewBox="0 0 11 9"><circle cx="5.5" cy="4.5" r="3.6" fill="none" stroke="var(--ink)" stroke-width="1.6"/><rect x="2" y="4" width="7" height="1.2" fill="var(--ink)"/></svg>WWW.YOURWEBSITE.COM</li>
    </ul>
  </div>
  <div class="watermark" aria-hidden="true">Tallo Goods</div>
  <span class="band band-bottom"><svg viewBox="0 0 611 45" preserveAspectRatio="none"><polygon points="0,0 338,0 304,45 0,45" fill="var(--brand-blue)"/><polygon points="344,0 611,0 611,45 310,45" fill="var(--brand-black)"/></svg></span>
  <div class="footer-url">WWW.YOURWEBSITE.COM</div>
</section>

<section class="piece card-front" aria-label="Business card front">
  <div class="wordmark">Tallo Goods</div>
</section>

<section class="piece card-back" aria-label="Business card back">
  <div class="wordmark">Tallo Goods</div>
  <div class="divider"></div>
  <div class="person"><div class="person-name">YOUR NAME.....</div><div class="person-role">Position</div></div>
  <ul class="contact-list">
    <li><svg viewBox="0 0 11 9"><path d="M0 3 Q5.5 -1 11 3 L9 4 L7.5 2.5 L3.5 2.5 L2 4 Z M2 5 H9 V9 H2 Z" fill="var(--ink)"/></svg>00 0000 0000</li>
    <li><svg viewBox="0 0 11 9"><rect x="0" y="1" width="11" height="7" fill="var(--ink)"/><path d="M0 1 L5.5 5 L11 1" stroke="#fff" fill="none"/></svg>INFO@TALLOGOODS.CO.NZ</li>
    <li><svg viewBox="0 0 11 9"><circle cx="5.5" cy="4.5" r="3.6" fill="none" stroke="var(--ink)" stroke-width="1.6"/><rect x="2" y="4" width="7" height="1.2" fill="var(--ink)"/></svg>WWW.TALLOGOODS.CO.NZ</li>
  </ul>
</section>

<section class="piece envelope-front" aria-label="Envelope front">
  <span class="band band-top"><svg viewBox="0 0 552 44" preserveAspectRatio="none"><polygon points="0,0 290,0 268,44 0,44" fill="var(--brand-blue)"/><polygon points="296,0 552,0 552,44 274,44" fill="var(--brand-black)"/></svg></span>
  <div class="wordmark">Tallo Goods</div>
  <div class="person"><div class="person-name">YOUR NAME.....</div><div class="person-role">Position</div></div>
  <ul class="contact-list">
    <li><svg viewBox="0 0 11 9"><path d="M0 3 Q5.5 -1 11 3 L9 4 L7.5 2.5 L3.5 2.5 L2 4 Z M2 5 H9 V9 H2 Z" fill="var(--ink)"/></svg>00 0000 0000</li>
    <li><svg viewBox="0 0 11 9"><rect x="0" y="1" width="11" height="7" fill="var(--ink)"/><path d="M0 1 L5.5 5 L11 1" stroke="#fff" fill="none"/></svg>EMAILADDRESS@DOMAIN.COM</li>
    <li><svg viewBox="0 0 11 9"><circle cx="5.5" cy="4.5" r="3.6" fill="none" stroke="var(--ink)" stroke-width="1.6"/><rect x="2" y="4" width="7" height="1.2" fill="var(--ink)"/></svg>WWW.YOURWEBSITE.COM</li>
  </ul>
  <span class="band band-bottom"><svg viewBox="0 0 552 26" preserveAspectRatio="none"><polygon points="0,0 290,0 276,26 0,26" fill="var(--brand-blue)"/><polygon points="296,0 552,0 552,26 282,26" fill="var(--brand-black)"/></svg></span>
</section>

<section class="piece envelope-back" aria-label="Envelope back">
  <svg class="flap-lines" viewBox="0 0 550 270" preserveAspectRatio="none" aria-hidden="true">
    <path d="M0 0 L250 110 Q275 120 300 110 L550 0" fill="none" stroke="#d6d9e0" stroke-width="1.5"/>
    <path d="M0 244 L200 120 M550 244 L350 120" fill="none" stroke="#e3e5ea" stroke-width="1.5"/>
  </svg>
  <div class="wordmark">Tallo Goods</div>
  <span class="band band-bottom"><svg viewBox="0 0 550 26" preserveAspectRatio="none"><polygon points="0,0 290,0 276,26 0,26" fill="var(--brand-blue)"/><polygon points="296,0 550,0 550,26 282,26" fill="var(--brand-black)"/></svg></span>
</section>

</body>
</html>
```